Flyer for the Lumen 2025 Conference

I am looking to produce a flyer for our upcoming conference, Lumen 2025. This is an annual conference that we plan to publicize on social media. The ideal designer will create a flyer that is eye-catching and effectively communicates the key information. Please see attached our logo, speaker photo, and flyer content.

Target Market(s)

All demographics

Industry/Entity Type

Christian

Font styles to use
Sans Serif

Requirements
Should not have
• Cross, church

```html
<!DOCTYPE html>
<html lang="en">
<head>
<meta charset="utf-8">
<title>Lumen 2025 Conference Flyer</title>
<link rel="stylesheet" href="https://fonts.googleapis.com/css2?family=Anton&family=Roboto:wght@400;500;700&display=swap">
<style>
  :root {
    --navy: #0d3a5f;
    --navy-deep: #0a2f4f;
    --orange: #f7941d;
    --white: #ffffff;
    --stage: #e6e6e6;
    --suit-blue: #2a6cc0;
  }
  * { margin: 0; padding: 0; box-sizing: border-box; }
  html, body {
    width: 1200px;
    height: 1200px;
    overflow: hidden;
    background: var(--stage);
  }
  body {
    position: relative;
    font-family: "Roboto", Arial, sans-serif;
    color: var(--white);
  }
  .flyer {
    position: absolute;
    left: 227px;
    top: 72px;
    width: 745px;
    height: 1055px;
    background: var(--navy);
    overflow: hidden;
  }
  .speaker-photo {
    position: absolute;
    left: 360px;
    top: 237px;
    width: 385px;
    height: 818px;
    background:
      radial-gradient(ellipse 60% 45% at 58% 52%, var(--suit-blue) 0%, rgba(42,108,192,0.55) 55%, rgba(13,58,95,0) 100%),
      linear-gradient(180deg, rgba(13,58,95,0) 0%, var(--navy-deep) 100%);
  }
  .brand {
    position: absolute;
    left: 520px;
    top: 66px;
    display: flex;
    align-items: center;
    gap: 10px;
  }
  .brand-dot {
    width: 18px;
    height: 18px;
    border-radius: 50%;
    background: var(--orange);
  }
  .brand-name {
    font-family: "Roboto", Arial, sans-serif;
    font-weight: 500;
    font-size: 40px;
    letter-spacing: 1px;
    color: var(--white);
  }
  .title {
    position: absolute;
    left: 44px;
    font-family: "Anton", Impact, sans-serif;
    line-height: 1;
  }
  .title-name {
    top: 62px;
    font-size: 148px;
    color: var(--white);
    letter-spacing: 2px;
  }
  .title-year {
    top: 192px;
    font-size: 196px;
    color: var(--orange);
    letter-spacing: 2px;
  }
  .subtitle-band {
    position: absolute;
    left: 0;
    top: 367px;
    width: 502px;
    height: 45px;
    background: var(--white);
  }
  .subtitle {
    position: absolute;
    left: 46px;
    top: 5px;
    font-size: 32px;
    font-weight: 400;
    color: var(--navy);
  }
  .details {
    position: absolute;
    left: 46px;
    top: 465px;
  }
  .detail { margin-bottom: 18px; }
  .detail-label {
    font-size: 23px;
    font-weight: 700;
    line-height: 1.15;
  }
  .detail-value {
    font-size: 14px;
    line-height: 1.3;
  }
  .download-button {
    position: absolute;
    left: 46px;
    top: 854px;
    width: 164px;
    height: 37px;
    border-radius: 7px;
    background: var(--orange);
    color: var(--navy);
    font-size: 22px;
    display: flex;
    align-items: center;
    justify-content: center;
  }
  .download-note {
    position: absolute;
    left: 46px;
    top: 903px;
    font-size: 14px;
  }
  .download-note strong { font-weight: 700; }
  .contact-line {
    position: absolute;
    left: 46px;
    top: 971px;
    display: flex;
    align-items: center;
    font-size: 14px;
  }
  .web-box {
    margin-left: 6px;
    padding: 3px 10px;
    background: var(--orange);
    color: var(--navy);
    font-weight: 700;
  }
</style>
</head>
<body>
  <main class="flyer">
    <div class="speaker-photo" role="img" aria-label="Photo of the speaker in a blue suit, seated on a wooden stool"></div>

    <div class="brand">
      <span class="brand-dot"></span>
      <span class="brand-name">KAVIRO</span>
    </div>

    <h1>
      <span class="title title-name">LUMEN</span>
      <span class="title title-year">2025</span>
    </h1>

    <div class="subtitle-band">
      <p class="subtitle">A Prophetic Conference</p>
    </div>

    <section class="details">
      <div class="detail">
        <p class="detail-label">Topic:</p>
        <p class="detail-value">The Voice Of The Lord</p>
      </div>
      <div class="detail">
        <p class="detail-label">Speaker:</p>
        <p class="detail-value">Prophet Elias Mwangi</p>
      </div>
      <div class="detail">
        <p class="detail-label">Date/Time</p>
        <p class="detail-value">Friday, December 26th, 6:30PM - 9:00PM</p>
        <p class="detail-value">Saturday, December 27th, 5:30PM&nbsp; - 8:00PM</p>
        <p class="detail-value">Sunday, December 29th, 4:30PM - 7:00PM</p>
      </div>
      <div class="detail">
        <p class="detail-label">Location</p>
        <p class="detail-value">The Harborview Performing Arts Center</p>
        <p class="detail-value">218 Millbrook Avenue</p>
        <p class="detail-value">Eastport, Maine 04631</p>
      </div>
    </section>

    <div class="download-button">Download&nbsp;▼</div>
    <p class="download-note">the <strong>KAVIRO App</strong> to stay updated on the event</p>

    <footer class="contact-line">
      <span>207 555 0142 | contact@kaviro.org</span>
      <span class="web-box">www.kaviro.org</span>
    </footer>
  </main>
</body>
</html>
```